KLVN- company with a mission

KLVN LLC stands for keeping lanterns vividly nigh (non profit arm is called lantern kept foundation)—our business is based out of New York City and has a non-profit arm where for every bar you purchase, we donate a bar (don’t want any designs that limits us to only soap). Currently working with South Africa. We want the focus to be organic/natural soap with a mission.
What our website needs to…achieve:
Purpose = branding, building up interesting leaving up to launch date, then a full functional site for selling soap (for now) with a mission. With that said, there will need to be a page designed for “COMING SOON” – with a place to post our teaser 30 second video (kind of like a commercial/movie trailer) – until everything else is done.
We are the first in the industry to do one for one (or …50/50). Most companies that do charity work are mostly for every $$$ we donate $0.10, or 1% of XXX. We are starting out to run the non-profit arm as well not just after we reach certain milestones. In addition, we will be transparent for the non-profit side whereas most of the time when you donate, you have no idea where the money ends up going.
IN ADDITION: we still need to be clean/elegant – and selling our soap; so website will need to 1. Showcase our products, 2. Be very clear that we have a mission (not sure if there is a way to show case both our soap AND our mission)
Some sites we like:
Pelarin.com—like them in terms of business model—in terms of their website: like how their site is clean and friendly, but it seems too cluttered
www.quendaltrove.com -- similar business model, www.fevriskel.com, brimavault.com, marshlintsoap.com
Tivel.com: like this a lot better than gavroue.com, however, major dislike of the typeface. Okay about the neutral colors…although feel like we need something a bit more cheerful here and there for our mission
Zkindle.net, brimavault.com, fennawick.com: like how they are clean and showcase well
**** However, our site also needs to convey messages like: www.wellspringpledge.org, www.rinsewidely.org
Looking for a clean, simple design. Modern, clutter-free, and inviting. Definitely do not want an arts and crafty/flowery feel. We do need something…cheerful for our nonprofit purposes.
Examples of sites we don’t like: quillmarbet.com, corvelpatchsoap.com
7 pages/ tabs maybe? (About us…video page (to show case what we are doing –currently my partner is in South Africa filming what our mission will be able to do – give children and those in need soap), FAQs, soap products, terms & conditions, contact us page, blog page……nothing too crazy).
For now, for designing purposes, please use any example texts whether it’s the about us page, mission page..policies.. and for the soap/products pages—please use example you can find online – it is fine, we just need the design done for now.
I have also attached our logo file. Please let me know if you have any questions! Thanks!
Something to consider....
pelarin.com and quendaltrove.com are probably our largest competitor out of all the websites I mentioned as they have a very similar business model where it is is a company with a mission. Homepage makes that clear that for every pair of shoes/ glasses you purchase, they give a pair. Another thing to note...is that they have been in business for a few years so their website probably have changed to more commercial than focusing/marketing on the mission of doing good. While we don't want that to be the total focus, we do need it to be present on the homepage/front page.

```html
<!DOCTYPE html>
<html lang="en">
<head>
<meta charset="utf-8">
<title>KLVN — Coming Soon</title>
<link rel="stylesheet" href="https://fonts.googleapis.com/css2?family=Cabin+Sketch:wght@700&family=Open+Sans:wght@400;600&display=swap">
<style>
  :root {
    --sky-top: #3f78b3;
    --sky-mid: #5aaedc;
    --sky-low: #86cdee;
    --cloud: #ffffff;
    --orange: #f4a261;
    --orange-dark: #e48c3e;
    --ink: #222222;
    --muted: #8a8a8a;
    --player-bar: #444444;
    --field-border: #cfcfcf;
    --placeholder: #b9b9b9;
  }
  * { box-sizing: border-box; margin: 0; padding: 0; }
  html, body { width: 1200px; height: 797px; overflow: hidden; }
  body { font-family: "Open Sans", Arial, sans-serif; color: var(--ink); }

  .page {
    position: relative;
    width: 1200px;
    height: 797px;
    overflow: hidden;
    background: radial-gradient(ellipse at 50% 85%, var(--sky-low) 0%, var(--sky-mid) 45%, var(--sky-top) 100%);
  }
  .sky-scene { position: absolute; inset: 0; }
  .cloud-bank { position: absolute; left: 0; bottom: 0; width: 1200px; height: 360px; }

  .brand-mark {
    position: absolute;
    left: 501px; top: 34px;
    width: 166px; height: 166px;
    border-radius: 50%;
    background: var(--orange);
    display: flex; align-items: center; justify-content: center;
  }
  .brand-name {
    font-family: "Open Sans", Arial, sans-serif;
    font-weight: 600;
    font-size: 44px;
    letter-spacing: 2px;
    color: #ffffff;
  }

  .headline {
    position: absolute;
    left: 0; top: 210px;
    width: 1244px;
    text-align: center;
    font-family: "Cabin Sketch", "Comic Sans MS", cursive;
    font-weight: 700;
    font-size: 96px;
    line-height: 1;
    color: #ffffff;
    letter-spacing: 2px;
  }

  .teaser-player {
    position: absolute;
    left: 108px; top: 336px;
    width: 632px; height: 408px;
    background: #ffffff;
    border-radius: 4px;
    box-shadow: 0 2px 8px rgba(0,0,0,0.28);
  }
  .teaser-player .big-play { position: absolute; left: 270px; top: 148px; width: 92px; height: 92px; }
  .controls {
    position: absolute;
    left: 21px; top: 362px;
    width: 590px; height: 25px;
    display: flex;
    background: var(--player-bar);
  }
  .controls .ctrl { width: 37px; height: 25px; background: var(--orange); display: flex; align-items: center; justify-content: center; }
  .controls .track { flex: 1; position: relative; }
  .controls .track-line { position: absolute; left: 10px; right: 40px; top: 8px; height: 9px; background: #ffffff; }
  .controls .track-buffer { position: absolute; left: 0; top: 0; width: 48px; height: 9px; background: #b0b0b0; }

  .signup { position: absolute; left: 775px; top: 511px; width: 300px; }
  .signup-title { font-size: 20px; font-weight: 400; line-height: 1.2; color: var(--ink); }
  .signup-sub { font-size: 14.5px; margin-top: 3px; color: #111111; }
  .email-field {
    display: block;
    margin-top: 17px; margin-left: 2px;
    width: 268px; height: 40px;
    border: 1px solid var(--field-border);
    border-radius: 3px;
    padding: 0 14px;
    font: 15px "Open Sans", Arial, sans-serif;
    color: var(--placeholder);
    line-height: 38px;
    background: #ffffff;
  }
  .notify-button {
    display: block;
    margin-top: 13px; margin-left: 3px;
    width: 116px; height: 40px;
    border: 0; border-radius: 2px;
    background: linear-gradient(var(--orange), var(--orange-dark));
    color: #ffffff;
    font: 15px "Open Sans", Arial, sans-serif;
  }
  .follow-label { margin-top: 20px; margin-left: 4px; font-size: 15px; color: var(--muted); }
  .social-links { display: flex; gap: 6px; margin-top: 8px; margin-left: 4px; }
  .social-dot { width: 28px; height: 28px; border-radius: 50%; background: var(--orange-dark); }
</style>
</head>
<body>
<main class="page">
  <div class="sky-scene" role="img" aria-label="Bright blue sky with soft light rays fanning out from the centre"></div>

  <svg class="cloud-bank" viewBox="0 0 1200 360" aria-hidden="true">
    <path fill="#ffffff" opacity="0.55" d="M0 150 C60 120 120 130 170 150 C700 150 720 140 760 130 C800 90 860 85 905 110 C940 80 1000 80 1040 115 C1100 100 1160 110 1200 130 L1200 360 L0 360 Z"/>
    <path fill="#ffffff" d="M0 170 C40 155 80 150 115 158 C150 140 190 150 210 165 L760 165 C790 135 830 125 870 140 C890 110 940 105 970 130 C1010 110 1060 115 1090 150 C1130 135 1170 140 1200 155 L1200 360 L0 360 Z"/>
  </svg>

  <div class="brand-mark"><span class="brand-name">KLVN</span></div>

  <h1 class="headline">Coming Soon</h1>

  <section class="teaser-player" aria-label="Teaser video">
    <svg class="big-play" viewBox="0 0 92 92" aria-hidden="true">
      <circle cx="46" cy="46" r="40" fill="none" stroke="#f4a261" stroke-width="10"/>
      <path d="M36 29 L64 46 L36 63 Z" fill="#f4a261"/>
    </svg>
    <div class="controls">
      <div class="ctrl"><svg width="12" height="13" viewBox="0 0 12 13"><path d="M1 0 L12 6.5 L1 13 Z" fill="#fff"/></svg></div>
      <div class="track"><div class="track-line"><div class="track-buffer"></div></div></div>
      <div class="ctrl"><svg width="18" height="14" viewBox="0 0 18 14"><rect x="1" y="1" width="16" height="12" fill="none" stroke="#fff" stroke-width="1.5"/><path d="M6 4 L12 10 M12 6 V10 H8" stroke="#fff" stroke-width="1.5" fill="none"/></svg></div>
    </div>
  </section>

  <section class="signup">
    <h2 class="signup-title">Enter Your Email Address and</h2>
    <p class="signup-sub">we’ll let you know as soon as it’s ready</p>
    <div class="email-field">example@domain.com</div>
    <button class="notify-button" type="button">Noify Me</button>
    <p class="follow-label">Follow Us</p>
    <div class="social-links">
      <span class="social-dot" role="img" aria-label="Social network link"></span>
      <span class="social-dot" role="img" aria-label="Social network link"></span>
      <span class="social-dot" role="img" aria-label="Video channel link"></span>
    </div>
  </section>
</main>
</body>
</html>
```